Business Card Design Project

Prime Swift Tasks- http:primeswifttasks.com./janetcorley

Industry/Entity Type

Business

Contact Information for Business Card

Well it could be a pretty color like a glossy pink look business type very Job related

```html
<!DOCTYPE html>
<html lang="en">
<head>
<meta charset="utf-8">
<title>Janet Corley – Business Card</title>
<link href="https://fonts.googleapis.com/css2?family=Cinzel:wght@400&family=Lato:wght@400&display=swap" rel="stylesheet">
<style>
  :root {
    --stage: #000000;
    --card-light: #ffffff;
    --card-dark: #3a3a3a;
    --card-dark-edge: #4a4a4a;
    --accent-pink: #e8175d;
    --ink: #2b2b2b;
    --ink-light: #e6e6e6;
    --rule: #c4c4c4;
  }
  * { margin: 0; padding: 0; box-sizing: border-box; }
  html, body {
    width: 1200px; height: 900px; overflow: hidden;
    background: var(--stage);
  }
  .stage { position: relative; width: 1200px; height: 900px; }
  .card {
    position: absolute; top: 300px; width: 442px; height: 273px;
    border-radius: 10px; text-align: center;
  }
  .card--front { left: 152px; background: var(--card-light); }
  .card--back { left: 612px; background: var(--card-dark); border: 1px solid var(--card-dark-edge); }

  .brand {
    position: absolute; left: 0; right: 0;
    display: flex; align-items: center; justify-content: center; gap: 10px;
    font-family: "Cinzel", serif; font-weight: 400;
    color: var(--accent-pink); letter-spacing: 1px;
  }
  .brand__square { border: 3px solid var(--accent-pink); }
  .card--front .brand { top: 56px; font-size: 20px; }
  .card--front .brand__square { width: 26px; height: 26px; }
  .card--back .brand { top: 95px; font-size: 22px; }
  .card--back .brand__square { width: 30px; height: 30px; }

  .holder-name {
    position: absolute; left: 0; right: 0;
    font-family: "Cinzel", serif; font-weight: 400; letter-spacing: 0.5px;
  }
  .card--front .holder-name { top: 120px; font-size: 27px; color: var(--ink); }
  .card--back .holder-name { top: 162px; font-size: 30px; color: var(--ink-light); }

  .divider {
    position: absolute; left: 132px; width: 178px; top: 170px;
    height: 1px; background: var(--rule);
  }
  .contact {
    position: absolute; left: 0; right: 0; top: 190px;
    list-style: none;
    font-family: "Lato", sans-serif; font-size: 13px; line-height: 18.5px;
    color: var(--ink);
  }
  .social {
    position: absolute; left: 0; right: 0; top: 214px;
    display: flex; justify-content: center; gap: 9px;
  }
  .social__dot {
    width: 22px; height: 22px; border-radius: 50%;
    border: 1.3px solid var(--accent-pink);
  }
</style>
</head>
<body>
<main class="stage">
  <section class="card card--front" aria-label="Card front">
    <div class="brand"><span class="brand__square"></span>Prime Swift Tasks</div>
    <h1 class="holder-name">Janet Corley</h1>
    <div class="divider"></div>
    <ul class="contact">
      <li>044-555 010 234</li>
      <li>INFO@PRIMESWIFTTASKS.COM</li>
      <li>WWW.PRIMESWIFTTASKS.COM</li>
    </ul>
  </section>

  <section class="card card--back" aria-label="Card back">
    <div class="brand"><span class="brand__square"></span>Prime Swift Tasks</div>
    <h2 class="holder-name">Janet Corley</h2>
    <div class="social" aria-label="Social profiles">
      <span class="social__dot"></span>
      <span class="social__dot"></span>
      <span class="social__dot"></span>
      <span class="social__dot"></span>
    </div>
  </section>
</main>
</body>
</html>
```